I need a business card design for a new dance business. I offer classical Indian dance tuition and also professional performances. I want to offer the community a variety of Indian dance experiences which include: group class and private tuition, school and preschool educational courses and workshops. dance theatre performances, community function workshops and performances, Kids Bollywood parties, wedding & conference performances, mouth percussion classes, Indian mythology/ dance costume and make up workshops.
The final design should communicate a feeling and impression of the vibrance and energy of Indian dance.
Updates
Hi Everyone,
Project Deadline Extended
Reason: I would like to refine a few changes to the details of this lovely design and we have run out of time!
Project Deadline Extended
Reason: Still waiting to hear back form designer re two possible changes to the card design. Tomorrow is the deadline and I have sent several messages but with no response. I need to see this through before selecting this lovely design.
Thank you.
Tara
Industry/Entity Type
Preschool
Requirements
Must have
- The front of the business card should have the photo of me (my face and torso), surrounded entirely by a border of bright magenta (to match the magenta of my lipstick - it is the same as the magenta on my skirt in the second photo). Within the top border I want (perhaps yellow-gold) writing to say "Tara Holloway - Artistic Director" and within the bottom border it should read "Silver Creek Kathak Studio." If you turn the card on its side the left border should have my telephone number: 0417 826 394 and the right-hand border should read: silvercreekkathakstudio@fernmail.example
The reverse of the card should be the orange of the dance costume
and I'd like the picture of my feet and legs to be on the right side of the back of the card as a side border. Centre-aligned on the orange background it should read (perhaps in dark magenta):
Indian dance classes + private tuition
School + preschool educational courses and workshops
Dance theatre performances
Community function workshops and performances
Children's Bollywood parties
Wedding + conference performances
Mouth percussion classes
Indian mythology and dance demonstration workshops
Dance costume and make-up workshops
Nice to have
- A lovely artistic but easy-to-read font would be nice.

```html
<!DOCTYPE html>
<html lang="en">
<head>
<meta charset="utf-8">
<title>Silver Creek Kathak Studio – Business Card</title>
<link rel="stylesheet" href="https://fonts.googleapis.com/css2?family=Alegreya+Sans:ital,wght@1,300;1,400&family=Crimson+Text:wght@400&display=swap">
<style>
  :root {
    --page: #ffffff;
    --plum: #7c1242;
    --plum-deep: #5e0c31;
    --gold: #f8d98a;
    --gold-bright: #ffe9a8;
    --glow: rgba(255, 190, 120, 0.75);
    --silk-pink: #c2188a;
    --silk-orange: #e9a23a;
    --skin: #d9a08a;
  }
  * { box-sizing: border-box; margin: 0; padding: 0; }
  html, body {
    width: 1200px; height: 900px; overflow: hidden;
    background: var(--page);
  }
  .sheet { position: relative; width: 1200px; height: 900px; }

  .card {
    position: absolute; top: 30px;
    width: 500px; height: 840px;
    background: radial-gradient(ellipse at 50% 40%, var(--plum) 0%, var(--plum-deep) 100%);
    box-shadow: 8px 10px 16px rgba(0,0,0,0.35);
    overflow: hidden;
  }
  .card--front { left: 80px; }
  .card--back { left: 630px; }

  .glow-text {
    color: var(--gold);
    text-shadow: 0 0 6px var(--glow), 0 0 14px rgba(255,120,90,0.5);
  }

  /* Front */
  .contact { position: absolute; top: 78px; left: 0; width: 100%; text-align: center;
    font-family: "Alegreya Sans", sans-serif; font-style: italic; }
  .contact__name { font-size: 36px; font-weight: 300; }
  .contact__role { font-size: 27px; font-weight: 300; margin-top: 6px; }
  .contact__phone { font-size: 29px; font-weight: 300; margin-top: 18px; font-style: normal; }

  .studio-name {
    position: absolute; left: 0; top: 318px; width: 100%;
    text-align: center;
    font-family: "Crimson Text", serif; font-weight: 400;
    font-size: 46px; line-height: 1.1;
    color: var(--gold);
  }
  .studio-email {
    position: absolute; left: 0; top: 428px; width: 100%;
    text-align: center;
    font-family: "Alegreya Sans", sans-serif; font-style: italic; font-weight: 400;
    font-size: 20px;
  }

  .portrait {
    position: absolute; left: 0; top: 470px; width: 500px; height: 370px;
    background: radial-gradient(closest-side at 50% 55%, var(--skin) 0%, var(--silk-orange) 45%, rgba(233,162,58,0.5) 75%, rgba(124,18,66,0) 100%);
  }

  /* Back */
  .feature {
    position: absolute; right: 0; top: 0; width: 240px; height: 840px;
    background: linear-gradient(180deg, var(--silk-pink) 0%, var(--silk-orange) 45%, var(--silk-pink) 70%, rgba(94,12,49,0) 100%);
    opacity: 0.9;
  }
  .back-title {
    position: absolute; left: 18px; top: 80px; width: 300px;
    font-family: "Crimson Text", serif; font-weight: 400;
    font-size: 36px; line-height: 1.15;
    color: var(--gold);
  }

  .services {
    position: absolute; left: 18px; top: 222px; width: 420px;
    list-style: none;
    font-family: "Crimson Text", serif; font-size: 20px; line-height: 1.3;
  }
  .services li { position: relative; padding-left: 20px; margin-bottom: 27px; color: var(--gold-bright); }
  .services li::before, .services li::after {
    content: ""; display: inline-block; width: 9px; height: 9px; border-radius: 50%;
    background: var(--gold);
  }
  .services li::before { position: absolute; left: 0; top: 10px; }
  .services li::after { margin-left: 8px; vertical-align: middle; }
</style>
</head>
<body>
<div class="sheet">

  <section class="card card--front">
    <div class="contact glow-text">
      <p class="contact__name">Tara Holloway</p>
      <p class="contact__role">Artistic Director</p>
      <p class="contact__phone">0417 826 394</p>
    </div>
    <p class="studio-name">Silver Creek<br>Kathak Studio</p>
    <p class="studio-email glow-text">silvercreekkathakstudio@fernmail.example</p>
    <div class="portrait" role="img" aria-label="Photo of the dancer in an orange and gold classical costume, hands raised in a dance pose"></div>
  </section>

  <section class="card card--back">
    <div class="feature" role="img" aria-label="Photo of a dancer's legs and feet in a magenta and gold costume with ankle bells"></div>
    <h2 class="back-title">Silver Creek<br>Kathak Studio</h2>
    <ul class="services glow-text">
      <li>Indian dance classes +<br>private tuition</li>
      <li>School + preschool educational<br>courses and workshops</li>
      <li>Dance theatre performances</li>
      <li>Community function<br>workshops and performances</li>
      <li>Children's Bollywood parties</li>
      <li>Wedding + conference performances</li>
      <li>Mouth percussion classes</li>
      <li>Indian mythology and dance<br>demonstration workshops</li>
      <li>Dance costume and make-up workshops</li>
    </ul>
  </section>

</div>
</body>
</html>
```